New Business Card

We need to refresh our business cards. We designed these ourselves and we have no graphic design experience. We would like to find a new business card design that is professional and unique. We are an auto finance company. Feel free to play with the logo, but we would like to keep the eye very present on the card. Our corporate colors are green, grey, and white.
Green - RGB - 168,215,27; HEX - #AADD22
Grey - RGB - 196,196,196; HEX - #C4C4C4
Need to upload the vector file to finalize the project. The last logo was for a jpeg that didn't stretch well.
Industry/Entity Type
Financial Service
Contact Information for Business Card
Honestly don't know...I need your help!

```html
<!DOCTYPE html>
<html lang="en">
<head>
<meta charset="utf-8">
<title>Northvale Capital – Business Card</title>
<link href="https://fonts.googleapis.com/css2?family=Source+Sans+3:wght@400;600&display=swap" rel="stylesheet">
<style>
  :root {
    --brand-green: #aadd22;
    --brand-grey: #c4c4c4;
    --paper: #ffffff;
    --ink-black: #000000;
    --backdrop: #e9e6e3;
  }
  * { margin: 0; padding: 0; box-sizing: border-box; }
  html, body { width: 1200px; height: 900px; overflow: hidden; }
  body {
    background: var(--backdrop);
    font-family: "Source Sans 3", "Myriad Pro", sans-serif;
    position: relative;
  }
  .card {
    position: absolute;
    overflow: hidden;
    box-shadow: 0 6px 18px rgba(0,0,0,0.18);
  }
  .card-front { left: 77px; top: 33px; width: 589px; height: 365px; background: var(--paper); }
  .card-back  { left: 388px; top: 505px; width: 567px; height: 352px; background: var(--ink-black); }

  .front-bands { position: absolute; inset: 0; }

  .wordmark {
    position: absolute;
    display: flex;
    align-items: center;
    gap: 16px;
    color: var(--brand-green);
    font-weight: 600;
    white-space: nowrap;
  }
  .wordmark-dot { border-radius: 50%; background: var(--brand-grey); flex: none; }
  .card-front .wordmark { left: 84px; top: 68px; font-size: 50px; }
  .card-front .wordmark-dot { width: 36px; height: 36px; }

  .contact-list {
    position: absolute; left: 30px; top: 256px;
    list-style: none; color: var(--paper); font-size: 15.5px; line-height: 21.5px;
  }
  .contact-list li { display: flex; align-items: center; gap: 8px; }
  .contact-list svg { width: 13px; height: 13px; fill: var(--paper); flex: none; }

  .person {
    position: absolute; right: 36px; top: 238px;
    text-align: right; color: var(--paper);
  }
  .person-name { font-size: 25px; line-height: 28px; font-weight: 400; }
  .person-title { font-size: 16px; line-height: 19px; }
  .person-address { margin-top: 10px; font-size: 15.5px; line-height: 21.5px; font-style: normal; }

  .card-back .wordmark {
    left: 0; right: 0; top: 180px; justify-content: center;
    font-size: 38px; gap: 12px;
  }
  .card-back .wordmark-dot { width: 28px; height: 28px; }
  .back-website {
    position: absolute; left: 0; right: 0; top: 294px;
    text-align: center; color: var(--paper); font-size: 15px;
  }
</style>
</head>
<body>

<section class="card card-front" aria-label="Business card front">
  <svg class="front-bands" width="589" height="365" viewBox="0 0 589 365" aria-hidden="true">
    <polygon points="0,194 392,194 366,219 0,219" fill="var(--brand-grey)"/>
    <polygon points="0,222 368,222 404,185 589,185 589,365 0,365" fill="var(--brand-green)"/>
  </svg>

  <div class="wordmark"><span class="wordmark-dot"></span>Northvale Capital</div>

  <ul class="contact-list">
    <li><svg viewBox="0 0 13 13"><path d="M3.5 0h6a1 1 0 0 1 1 1v11a1 1 0 0 1-1 1h-6a1 1 0 0 1-1-1V1a1 1 0 0 1 1-1zm.5 2v8h5V2zm2.5 8.6a.7.7 0 1 0 0 1.4.7.7 0 0 0 0-1.4z"/></svg>044-555 210 347</li>
    <li><svg viewBox="0 0 13 13"><path d="M1 4c0-2 2-3 5.5-3S12 2 12 4v1H9V3.8C8 3.5 5 3.5 4 3.8V5H1zm2 2h7l2 3v3H1V9zm3.5 1.5a1.5 1.5 0 1 0 0 3 1.5 1.5 0 0 0 0-3z"/></svg>044-555 210 347</li>
    <li><svg viewBox="0 0 13 13"><path d="M0 2.5h13v8H0zm1 .8v.4l5.5 3.6L12 3.7v-.4zm0 1.6V9.7h11V4.9L6.5 8.5z"/></svg>info@northvale.com</li>
    <li><svg viewBox="0 0 13 13"><path d="M6.5 0a6.5 6.5 0 1 0 0 13 6.5 6.5 0 0 0 0-13zM4 3c1 0 2 .8 1.6 1.8-.3.8-1.6.6-1.6 1.7 0 1 1.5 1 1.5 2.3 0 1-.6 2-.6 2.6A5 5 0 0 1 2.3 3.4C2.8 3.2 3.4 3 4 3zm4.5-.9A5 5 0 0 1 11.4 8c-.6-.5-1.3-.3-1.8-1-.5-.8.2-1.5-.5-2.2-.6-.6-1.6-.3-1.6-1.2 0-.6.5-1 1-1.5z"/></svg>www.northvalecapital.com</li>
  </ul>

  <div class="person">
    <h1 class="person-name">Daniel Reyes</h1>
    <p class="person-title">Managing Director</p>
    <address class="person-address">48 Harbour Street<br>Westfield, 204518.</address>
  </div>
</section>

<section class="card card-back" aria-label="Business card back">
  <div class="wordmark"><span class="wordmark-dot"></span>Northvale Capital</div>
  <p class="back-website">www.northvalecapital.com</p>
</section>

</body>
</html>
```